New and exciting team challenge starting in corporate health. Need a eye catching flyer

Brisk Office Quest- http://www.briskofficequest.com. Is a new corporate team wellness program that uses a innovative online platform to track and record users active lifestyle choices. We require a flyer for initial promotion and create a buzz.

Participants goal is to log as many active points as you can on the BOQ APP by completing individual and team challenges and making healthy, active lifestyle choices. The more points you log the closer your team will get to unlocking all 15 Active Levels throughout the 10 week challenge. Each level unlocks information on ancient warrior tribes like the Amazonians. There are plenty of extra trophies to be won along the way, like the ‘Sunny Fern’ award for active travel and healthy eating.

Tag line- Your next challenge is here
Final design should leave them wanting more to check out the website. The target will be for those currently exercising. so needs to rope them in with the challenges
Join the Brisk Office Quest
- Get rewarded for healthy lifestyle choices daily on the BOQ App
- Compete against teams across Australia and see where you rank
- Complete fun weekly challenges like Peak Rattler and Steep Voltmark
- Ask Exercise Physiologists and Dietitians all your big questions
- Access 1000’s of exercise programs & videos or create your own and share
- Be a HEALTHIER & HAPPIER YOU

www.briskofficequest.com.au

for more of an idea check out: https://www.vidhubstream.com/watch?v=Qk7TzpLmB3x

Designer payment is now committed! look forward to seeing some cool designs.

Hi Everybody, Thanks for your work so far. I have made a small change to the design brief so please have a look. key features has now changed to below- Join the Brisk Office Quest to - Get rewarded for healthy lifestyle choices daily on the BOQ App - Compete against teams across the challenge and see where you rank - Complete fun weekly challenges like Peak Rattler and Steep Voltmark - Ask Exercise Physiologists and Dieticians all your big questions - Access 1000’s of exercise programs & videos or create your own and share

Target Market(s)

Active individuals 30-55yrs old that want to be challenged physically in a fun team environment.
Targeting corporate organisations.

Industry/Entity Type

Travel

Requirements
Must have
• simple and clear to read
Register your interest at www.briskofficequest.com.au
logo
'Your next challenge is here'
' Starts 16th of March'
Find us on Facebook and twitter (use symbols)

Nice to have
• 'The wellness program that challenges, educates and transforms organisations health behaviors'
'What's your lifestyle score?
Should not have
• too many words.

```html
<!DOCTYPE html>
<html lang="en">
<head>
<meta charset="utf-8">
<title>Brisk Office Quest – Flyer</title>
<link href="https://fonts.googleapis.com/css2?family=Josefin+Sans:wght@300;400;700&family=Open+Sans:ital,wght@0,400;0,600;0,800;1,400;1,800&display=swap" rel="stylesheet">
<style>
  :root {
    --stage: #e4e4e4;
    --paper: #ffffff;
    --ink: #23253f;
    --grey: #5a5a5a;
    --orange: #f15a24;
    --green: #63b35f;
    --green-dark: #4e9d4b;
    --white: #ffffff;
  }
  * { box-sizing: border-box; margin: 0; padding: 0; }
  html, body { width: 1200px; height: 1000px; overflow: hidden; }
  body { background: var(--stage); font-family: "Open Sans", sans-serif; }

  .flyer {
    position: absolute; left: 80px; top: 150px;
    width: 1040px; height: 700px;
    background: var(--paper);
    box-shadow: 0 10px 30px rgba(0,0,0,.18);
    overflow: hidden;
  }
  .hero-photo {
    position: absolute; left: 0; top: 0; width: 1040px; height: 590px;
    background:
      linear-gradient(180deg, rgba(255,255,250,.95) 0%, rgba(255,255,250,.55) 30%, rgba(255,255,250,0) 55%),
      linear-gradient(160deg, #f4f0d8 0%, #e6dcb4 40%, #b9a27a 75%, #8a7458 100%);
  }
  .headline {
    position: absolute; left: 40px; top: 30px;
    font-family: "Josefin Sans", sans-serif; font-weight: 300;
    font-size: 44px; letter-spacing: 5px; color: var(--grey);
  }
  .mission {
    position: absolute; left: 42px; top: 88px; width: 560px;
    font-style: italic; font-size: 17px; line-height: 1.25; color: var(--grey);
  }
  .start-date {
    position: absolute; left: 42px; top: 140px;
    font-weight: 800; font-style: italic; font-size: 21px; color: var(--orange);
  }
  .start-date sup { font-size: 12px; }
  .offer-title {
    position: absolute; left: 42px; top: 185px;
    font-weight: 800; font-size: 30px; letter-spacing: 1px; color: var(--ink);
  }
  .offer-list {
    position: absolute; left: 42px; top: 232px; width: 820px;
    list-style: none; font-size: 16px; line-height: 1.35; color: var(--ink);
  }
  .tagline {
    position: absolute; left: 40px; top: 345px; color: var(--white);
    font-family: "Josefin Sans", sans-serif;
    text-shadow: 0 2px 8px rgba(0,0,0,.25);
  }
  .tagline-lead { display: block; font-weight: 300; font-size: 60px; letter-spacing: 4px; }
  .tagline-punch { display: block; font-weight: 700; font-size: 104px; line-height: .95; letter-spacing: 3px; }

  .web-band {
    position: absolute; left: 0; top: 560px; width: 570px; height: 62px;
    background: var(--green); display: flex; align-items: center; padding-left: 28px;
  }
  .web-address {
    font-family: "Josefin Sans", sans-serif; font-weight: 300;
    font-size: 34px; letter-spacing: 1px; color: var(--white);
  }
  .social-tab {
    position: absolute; left: 320px; top: 622px; width: 250px; height: 48px;
    background: var(--green-dark); display: flex; align-items: center; gap: 12px; padding-left: 20px;
  }
  .social-label { font-size: 13px; font-style: italic; color: var(--white); }
  .social-dot { width: 20px; height: 20px; border-radius: 50%; background: var(--white); }

  .brand-box {
    position: absolute; right: 120px; top: 505px; width: 280px; height: 150px;
    background: var(--paper); box-shadow: 0 4px 14px rgba(0,0,0,.2);
    display: flex; align-items: center; justify-content: center; gap: 14px;
  }
  .brand-square { width: 34px; height: 34px; border-radius: 6px; background: var(--green); }
  .brand-name {
    font-family: "Josefin Sans", sans-serif; font-weight: 700;
    font-size: 28px; line-height: 1.05; color: var(--orange); text-transform: uppercase;
  }
</style>
</head>
<body>
  <main class="flyer">
    <div class="hero-photo" role="img" aria-label="Man with raised arm overlooking a hazy city skyline at sunrise"></div>

    <h1 class="headline">WHAT'S YOUR LIFESTYLE SCORE?</h1>
    <p class="mission">The wellness program that challenges, educates<br>and transforms organisations health behaviors</p>
    <p class="start-date">Starts 16<sup>th</sup> of March</p>

    <h2 class="offer-title">WHAT WE OFFER</h2>
    <ol class="offer-list">
      <li>1.Weekly individual and team challenges including Steep Voltmark and Peak Rattler.</li>
      <li>2.Stock your trophy cabinet with over 25 awards</li>
      <li>3.1000's of workouts to suit your goals</li>
      <li>4.15 Active Lifestyle levels to work your way through</li>
      <li>5.Have all your health and fitness questions answered by qualified dietitians, exercise physiologists.</li>
    </ol>

    <p class="tagline">
      <span class="tagline-lead">YOUR NEXT CHALLENGE</span>
      <span class="tagline-punch">IS HERE...</span>
    </p>

    <div class="web-band"><span class="web-address">www.briskofficequest.com.au</span></div>
    <div class="social-tab">
      <span class="social-label">Follow us on</span>
      <span class="social-dot"></span>
      <span class="social-dot"></span>
    </div>

    <div class="brand-box">
      <span class="brand-square"></span>
      <span class="brand-name">Brisk Office<br>Quest</span>
    </div>
  </main>
</body>
</html>
```